ZRD Roofing Billboard Design

Looking for a fresh new billboard design with my new headshot photo and using some info from my previous billboard and maybe website for design/content inspiration. My website is https://zrdroofing.com/

Also attached are my logo and current lawn sign design. I am looking for something simple, clean and modern. The landing page website should be 3816tops.com like my previous billboard has.

```html
<!DOCTYPE html>
<html lang="en">
<head>
<meta charset="utf-8">
<title>ZRD Roofing Billboard</title>
<link href="https://fonts.googleapis.com/css2?family=Oswald:wght@500;600;700&display=swap" rel="stylesheet">
<style>
  :root {
    --page-bg: #e6e6e6;
    --navy: #1f3560;
    --navy-deep: #1a2d52;
    --green: #3aaa55;
    --green-bright: #45b562;
    --white: #ffffff;
    --ink: #1f3560;
  }
  html, body {
    margin: 0;
    padding: 0;
    width: 1200px;
    height: 1200px;
    overflow: hidden;
    background: var(--page-bg);
  }
  .canvas {
    position: relative;
    width: 1200px;
    height: 1200px;
  }
  .billboard {
    position: absolute;
    left: 123px;
    top: 461px;
    width: 954px;
    height: 278px;
    box-shadow: 0 18px 28px rgba(0,0,0,0.35);
  }
  .billboard svg { display: block; }
  .headline, .price, .contact, .brand-name {
    font-family: "Oswald", sans-serif;
  }
  .headline-main { font-weight: 700; font-size: 64px; fill: var(--white); }
  .headline-sub { font-weight: 600; font-size: 44px; fill: var(--green-bright); }
  .headline-lead { font-weight: 600; font-size: 37px; fill: var(--white); }
  .price { font-weight: 600; font-size: 50px; fill: var(--white); }
  .contact { font-weight: 600; font-size: 24px; fill: var(--ink); }
  .brand-name { font-weight: 500; font-size: 24px; fill: var(--white); }
</style>
</head>
<body>
<main class="canvas">
  <section class="billboard" aria-label="ZRD Roofing billboard">
    <svg width="954" height="278" viewBox="0 0 954 278" xmlns="http://www.w3.org/2000/svg">
      <defs>
        <linearGradient id="bg-base" x1="0" y1="0" x2="1" y2="0.3">
          <stop offset="0" stop-color="#3aa558"/>
          <stop offset="0.22" stop-color="#1e3a66"/>
          <stop offset="0.6" stop-color="#1d3560"/>
          <stop offset="0.85" stop-color="#2e6a58"/>
          <stop offset="1" stop-color="#3aa558"/>
        </linearGradient>
        <linearGradient id="house-fill" x1="0" y1="0" x2="1" y2="1">
          <stop offset="0" stop-color="#3d4b63" stop-opacity="0.2"/>
          <stop offset="0.5" stop-color="#8f99a8" stop-opacity="0.55"/>
          <stop offset="1" stop-color="#4c5a6e" stop-opacity="0.4"/>
        </linearGradient>
        <linearGradient id="person-fill" x1="0" y1="0" x2="0" y2="1">
          <stop offset="0" stop-color="#3a4a52"/>
          <stop offset="0.35" stop-color="#8c6d5c"/>
          <stop offset="0.55" stop-color="#b9cbe4"/>
          <stop offset="1" stop-color="#a9bddb"/>
        </linearGradient>
      </defs>

      <rect class="backdrop" x="0" y="0" width="954" height="278" fill="url(#bg-base)"/>

      <rect class="house-photo" x="440" y="0" width="360" height="230" fill="url(#house-fill)"
            role="img" aria-label="Photo of a large house with a new grey shingle roof"/>

      <rect class="headshot-photo" x="662" y="0" width="292" height="278" fill="url(#person-fill)" opacity="0.9"
            role="img" aria-label="Headshot of the company owner in a light blue shirt, smiling"/>

      <g class="contact-band">
        <polygon points="0,200 632,236 662,238 662,278 0,278" fill="var(--green)"/>
        <polygon points="0,207 632,243 662,245 662,278 0,278" fill="var(--white)"/>
      </g>

      <g class="brand">
        <circle cx="110" cy="100" r="46" fill="none" stroke="var(--white)" stroke-width="3"/>
        <text class="brand-name" x="110" y="172" text-anchor="middle">ZRD Roofing</text>
      </g>

      <g class="headline">
        <text class="headline-main" x="240" y="81">FULL ROOF</text>
        <text class="headline-sub" x="240" y="129">REPLACEMENTS</text>
        <text class="headline-lead" x="240" y="190">STARTING AT</text>
      </g>

      <g class="price-tag">
        <polygon points="474,146 617,146 617,225 632,251 600,215 474,215" fill="var(--green)"/>
        <text class="price" x="545" y="204" text-anchor="middle">$7,499</text>
      </g>

      <g class="contact-web">
        <g fill="none" stroke="var(--green)" stroke-width="1.8">
          <circle cx="25" cy="254" r="9"/>
          <ellipse cx="25" cy="254" rx="4" ry="9"/>
          <line x1="16" y1="254" x2="34" y2="254"/>
        </g>
        <text class="contact" x="52" y="263">3816tops.com</text>
      </g>

      <g class="contact-phone">
        <path d="M255,245 l4,-1 l3,6 l-3,2 q2,5 7,8 l2,-3 l6,3 l-1,4 q-3,3 -8,0 q-9,-6 -12,-13 q-1,-4 2,-6z"
              fill="none" stroke="var(--green)" stroke-width="1.8" stroke-linejoin="round"/>
        <text class="contact" x="289" y="262">(555) 214-7306</text>
      </g>
    </svg>
  </section>
</main>
</body>
</html>
```